Food packaging label design

The product name Crispelle, a thin, crispy, and delicious biscuit/cookie made from simple, all natural ingredients. Its name comes from the fact that it looks and tastes a lot like a biscotti cookie, but thinly sliced and much crispier and more delicious than a biscotti. There are currently two flavors: Pure Nutlets, and Almond Cranberry.

I am looking for a fresh, eye catchy design to go on the label for a rice paper stand up pouch (pouch sample attached). Label size are as follows:

4 oz bag - Width X Height
top: 4.5" x 3.5" bottom: 4.5" x 1.5"

12 oz bag
top: 6.5" x 5.5" bottom: 6.5" x 1.5"

I would like for the top portion of the packaging to include:

Crispelle name
Tag line " a thinner, crispier, and more delicious cousin to the biscotti"
simple and natural ingredients

bottom to include:
net weight
ingredients: wheat flour, eggs, sugar, almonds

Attached is a copy of something I created in powerpoint. you can recreate this using graphic designer software per label specs and improve on it or supprise me with something totally awesome. The key is that it that the colors and design needs to pop or contrast against the white rice paper bag and design needs to be eye catchy, fun and whimsical.

Please refer to link below for best practices for creating artwork for labels to ensure correct format for printing.
http://www.vantorprint.example/label-articles/best-practices-designing-custom-labels/

Good luck!

Target Market(s)

educated, health conscious consumers such as customers who shops at meadow pantry, brewvane, market hollis

Industry/Entity Type

Graphic Designer

Requirements
Should not have
• busy or clutter design

```html
<!DOCTYPE html>
<html lang="en">
<head>
<meta charset="utf-8">
<title>Crispelle – Almond Cranberry label</title>
<link rel="stylesheet" href="https://fonts.googleapis.com/css2?family=Gochi+Hand&family=Patrick+Hand&display=swap">
<style>
  :root {
    --amber-deep: #b4681c;
    --amber: #d99a3a;
    --gold: #c9982e;
    --brown: #5a3510;
    --paper: #ffffff;
    --ink: #1c1408;
  }
  * { margin: 0; padding: 0; box-sizing: border-box; }
  html, body { width: 808px; height: 1200px; overflow: hidden; background: var(--paper); }
  .label {
    position: relative;
    width: 808px;
    height: 1200px;
    overflow: hidden;
    background:
      radial-gradient(ellipse 120px 140px at 60px 420px, rgba(127,154,58,.55), transparent 70%),
      radial-gradient(ellipse 140px 120px at 760px 40px, rgba(192,57,43,.6), transparent 70%),
      radial-gradient(ellipse 160px 200px at 770px 640px, rgba(217,120,40,.55), transparent 70%),
      linear-gradient(180deg, var(--amber-deep) 0%, var(--amber) 20%, #e8c27a 38%, #fbf3e2 52%, var(--paper) 62%, var(--paper) 82%, #f0d9a8 90%, var(--amber) 100%);
    font-family: "Patrick Hand", cursive;
  }
  .brand-name {
    position: absolute;
    top: 118px;
    left: 0;
    width: 100%;
    text-align: center;
    font-family: "Gochi Hand", cursive;
    font-weight: 400;
    font-size: 124px;
    line-height: 1;
    color: var(--paper);
    -webkit-text-stroke: 2px var(--brown);
    paint-order: stroke fill;
  }
  .product-art { position: absolute; left: 0; top: 0; }
  .tagline-text {
    font-family: "Patrick Hand", cursive;
    font-size: 36px;
    fill: var(--paper);
    stroke: var(--brown);
    stroke-width: 5px;
    paint-order: stroke;
    stroke-linejoin: round;
  }
  .flavor-text {
    font-family: "Patrick Hand", cursive;
    font-size: 32px;
    fill: var(--paper);
    stroke: var(--brown);
    stroke-width: 4px;
    paint-order: stroke;
  }
  .pack-info {
    position: absolute;
    right: 40px;
    top: 1024px;
    text-align: right;
    color: var(--ink);
    line-height: 1.05;
  }
  .net-weight { font-size: 24px; margin-right: 50px; }
  .ingredients-heading { font-size: 26px; }
  .ingredients-list { font-size: 15px; }
  .crimp-note {
    position: absolute;
    bottom: 30px;
    left: 0;
    width: 100%;
    text-align: center;
    font-family: Arial, Helvetica, sans-serif;
    font-size: 12px;
    color: #3a2a10;
  }
</style>
</head>
<body>
<main class="label">
  <h1 class="brand-name">Crispelle</h1>

  <svg class="product-art" width="808" height="1200" viewBox="0 0 808 1200">
    <defs>
      <linearGradient id="cookie-tones" x1="0" y1="0" x2="1" y2="1">
        <stop offset="0" stop-color="#efe0bd"/>
        <stop offset=".5" stop-color="#e3cc98"/>
        <stop offset="1" stop-color="#cfae72"/>
      </linearGradient>
      <linearGradient id="gold-band" x1="0" y1="0" x2="1" y2="0">
        <stop offset="0" stop-color="#c9982e" stop-opacity=".1"/>
        <stop offset=".2" stop-color="#c9982e"/>
        <stop offset=".8" stop-color="#c9982e"/>
        <stop offset="1" stop-color="#c9982e" stop-opacity=".1"/>
      </linearGradient>
      <path id="tagline-path" d="M216 640 A185 330 0 1 1 497 1000"/>
    </defs>

    <ellipse class="photo-window" cx="395" cy="725" rx="165" ry="305"
             fill="url(#cookie-tones)" role="img"
             aria-label="Photo of thin sliced almond cranberry crisps piled together"/>
    <ellipse class="photo-frame" cx="395" cy="725" rx="165" ry="305"
             fill="none" stroke="#c9982e" stroke-width="7"/>

    <text class="tagline-text">
      <textPath href="#tagline-path" textLength="990" lengthAdjust="spacing">a thinner, crispier, and more delicious cousin to the biscotti!</textPath>
    </text>

    <rect class="flavor-band" x="140" y="762" width="220" height="56" rx="6" fill="url(#gold-band)"/>
    <text class="flavor-text" x="250" y="801" text-anchor="middle">Almond Cranberry</text>
  </svg>

  <section class="pack-info">
    <p class="net-weight">net weight 6 oz.</p>
    <p class="ingredients-heading">Simple natural ingredients:</p>
    <p class="ingredients-list">wheat flour, eggs, sugar, almonds</p>
  </section>

  <p class="crimp-note">This area is the bottom crimp</p>
</main>
</body>
</html>
```